"Thornbury Accupuncture" needs a Promotional Card - A6 size

Requirements
Must have
• Bright colours, pictures of happy people, acupuncture-related pictures.

```html
<!DOCTYPE html>
<html lang="en">
<head>
<meta charset="utf-8">
<title>Thornbury Accupuncture – Promotional Cards</title>
<link href="https://fonts.googleapis.com/css2?family=Open+Sans:wght@400;600;700&display=swap" rel="stylesheet">
<style>
  :root {
    --orange: #e8461f;
    --yellow: #f5d630;
    --ink: #2b2b2b;
    --grey: #555555;
    --paper: #ffffff;
    --backdrop: #ececea;
    --sand: #e9d9c0;
    --sky: #b9d2e3;
    --sea: #7fa9c2;
    --skin: #f1d7c6;
    --garden: #b8c79a;
  }
  * { box-sizing: border-box; margin: 0; padding: 0; }
  html, body { width: 1200px; height: 895px; overflow: hidden; }
  body {
    background: var(--backdrop);
    font-family: "Open Sans", Arial, sans-serif;
    color: var(--ink);
    position: relative;
  }
  .card {
    position: absolute;
    background: var(--paper);
    overflow: hidden;
    box-shadow: 0 3px 10px rgba(0,0,0,.18);
  }
  .card--front { left: 90px; top: 88px; width: 495px; height: 700px; }
  .card--back { left: 625px; top: 122px; width: 495px; height: 700px; }

  .hero { position: absolute; left: 0; top: 0; width: 100%; }
  .wordmark {
    position: absolute;
    color: var(--orange);
    font-weight: 700;
    line-height: 1;
    text-align: center;
    letter-spacing: -0.5px;
  }
  .card--front .wordmark { right: 20px; top: 78px; font-size: 25px; }
  .card--back .wordmark { right: 14px; top: 200px; font-size: 25px; }

  .bottom-bar { position: absolute; left: 0; bottom: 0; width: 100%; height: 14px; background: var(--orange); }

  /* front */
  .headline {
    position: absolute; left: 0; top: 182px; width: 100%;
    text-align: center; color: var(--orange);
    font-size: 22px; font-weight: 600; line-height: 30px;
  }
  .question {
    position: absolute; left: 0; top: 250px; width: 100%;
    text-align: center; color: var(--ink); font-size: 17.5px;
  }
  .symptoms {
    position: absolute; list-style: none;
    font-size: 16.5px; color: var(--grey); line-height: 25px;
  }
  .symptoms--a { left: 45px; top: 298px; }
  .symptoms--b { left: 254px; top: 294px; }
  .symptoms li { display: flex; align-items: center; gap: 5px; }
  .bullet { width: 12px; height: 12px; flex: none; }
  .intro {
    position: absolute; left: 28px; top: 436px; width: 447px;
    font-size: 13.2px; line-height: 18px; text-align: justify; color: var(--ink);
  }
  .offer {
    position: absolute; left: 0; top: 540px; width: 100%; height: 88px;
    background: var(--yellow); color: var(--orange);
    font-size: 16px; font-weight: 700; line-height: 20px;
    text-align: center; padding-top: 17px;
  }
  .contact-row {
    position: absolute; left: 28px; top: 648px; width: 440px;
    display: flex; justify-content: space-between; font-size: 16.5px;
  }
  .contact-row span, .contact-list li { display: flex; align-items: center; gap: 6px; }

  /* back */
  .section-title {
    position: absolute; left: 24px; color: var(--orange);
    font-size: 16.5px; font-weight: 700;
  }
  .section-body { position: absolute; left: 24px; font-size: 13px; line-height: 18px; color: var(--ink); }
  .what-title { top: 264px; }
  .what-body { top: 286px; width: 450px; }
  .about-title { top: 377px; }
  .about-body { top: 399px; width: 292px; text-align: justify; }
  .about-body p + p { margin-top: 18px; }
  .thumb {
    position: absolute; left: 345px; width: 134px; height: 91px;
    border: 1px solid var(--yellow);
  }
  .thumb--back { top: 380px; background: radial-gradient(circle at 55% 55%, #f0a090 0 12%, var(--skin) 40%, #f7ece4 100%); }
  .thumb--hand { top: 480px; background: linear-gradient(135deg, #f8ece4, var(--skin) 55%, #e6b9a0); }
  .thumb--needles { top: 581px; background: linear-gradient(120deg, #ffffff, var(--skin) 60%, #d9b6a2); }
  .portrait {
    position: absolute; left: 0; top: 565px; width: 106px; height: 121px;
    background: linear-gradient(180deg, #e7e5e2, #b79a8a 70%, #6d4a52);
  }
  .practitioner { position: absolute; left: 110px; top: 558px; }
  .practitioner-name { color: var(--orange); font-size: 16.5px; }
  .credentials { font-size: 10.5px; margin-top: 2px; }
  .contact-list {
    position: absolute; left: 110px; top: 624px; list-style: none;
    font-size: 12px; line-height: 16px;
  }
  .icon { flex: none; }
</style>
</head>
<body>

<!-- Front card -->
<section class="card card--front">
  <svg class="hero" width="495" height="160" viewBox="0 0 495 160">
    <defs>
      <linearGradient id="beach" x1="0" y1="0" x2="0" y2="1">
        <stop offset="0" stop-color="var(--sky)"/>
        <stop offset=".45" stop-color="var(--sea)"/>
        <stop offset=".75" stop-color="var(--sand)"/>
      </linearGradient>
      <linearGradient id="beachFade" x1="0" y1="0" x2="1" y2="0">
        <stop offset=".35" stop-color="#fff" stop-opacity="0"/>
        <stop offset=".7" stop-color="#fff" stop-opacity="1"/>
      </linearGradient>
    </defs>
    <g role="img" aria-label="Photo of an older couple walking hand in hand along a sunny beach">
      <rect width="495" height="160" fill="url(#beach)"/>
      <rect width="495" height="160" fill="url(#beachFade)"/>
    </g>
    <path d="M0 72 C70 60 110 120 200 118 C300 116 380 155 495 125 L495 160 L0 160 Z" fill="var(--yellow)"/>
    <path d="M0 112 C90 100 130 148 230 146 C330 144 400 160 495 142 L495 160 L0 160 Z" fill="var(--paper)"/>
  </svg>
  <div class="wordmark">thornbury<br>accupuncture</div>

  <h1 class="headline">Chinese medicine &amp; acupuncture<br>can improve your well-being</h1>
  <p class="question">Do you suffer from any of the following?</p>

  <ul class="symptoms symptoms--a">
    <li><svg class="bullet" viewBox="0 0 12 12"><circle cx="6" cy="6" r="6" fill="var(--orange)"/><path d="M5 3.5 7.5 6 5 8.5" stroke="#fff" stroke-width="1.6" fill="none"/></svg>Anxiety</li>
    <li><svg class="bullet" viewBox="0 0 12 12"><circle cx="6" cy="6" r="6" fill="var(--orange)"/><path d="M5 3.5 7.5 6 5 8.5" stroke="#fff" stroke-width="1.6" fill="none"/></svg>Problems walking</li>
    <li><svg class="bullet" viewBox="0 0 12 12"><circle cx="6" cy="6" r="6" fill="var(--orange)"/><path d="M5 3.5 7.5 6 5 8.5" stroke="#fff" stroke-width="1.6" fill="none"/></svg>Chronic pain</li>
    <li><svg class="bullet" viewBox="0 0 12 12"><circle cx="6" cy="6" r="6" fill="var(--orange)"/><path d="M5 3.5 7.5 6 5 8.5" stroke="#fff" stroke-width="1.6" fill="none"/></svg>Depression</li>
    <li><svg class="bullet" viewBox="0 0 12 12"><circle cx="6" cy="6" r="6" fill="var(--orange)"/><path d="M5 3.5 7.5 6 5 8.5" stroke="#fff" stroke-width="1.6" fill="none"/></svg>Insomnia</li>
  </ul>
  <ul class="symptoms symptoms--b">
    <li><svg class="bullet" viewBox="0 0 12 12"><circle cx="6" cy="6" r="6" fill="var(--orange)"/><path d="M5 3.5 7.5 6 5 8.5" stroke="#fff" stroke-width="1.6" fill="none"/></svg>Stress</li>
    <li><svg class="bullet" viewBox="0 0 12 12"><circle cx="6" cy="6" r="6" fill="var(--orange)"/><path d="M5 3.5 7.5 6 5 8.5" stroke="#fff" stroke-width="1.6" fill="none"/></svg>PMS</li>
    <li><svg class="bullet" viewBox="0 0 12 12"><circle cx="6" cy="6" r="6" fill="var(--orange)"/><path d="M5 3.5 7.5 6 5 8.5" stroke="#fff" stroke-width="1.6" fill="none"/></svg>Arthritis</li>
    <li><svg class="bullet" viewBox="0 0 12 12"><circle cx="6" cy="6" r="6" fill="var(--orange)"/><path d="M5 3.5 7.5 6 5 8.5" stroke="#fff" stroke-width="1.6" fill="none"/></svg>Headache</li>
    <li><svg class="bullet" viewBox="0 0 12 12"><circle cx="6" cy="6" r="6" fill="var(--orange)"/><path d="M5 3.5 7.5 6 5 8.5" stroke="#fff" stroke-width="1.6" fill="none"/></svg>Menopausal symptoms</li>
  </ul>

  <p class="intro">Mira Kostova is a qualified acupuncturist who has helped many clients with these conditions. To learn more about the current research into acupuncture for these and other conditions, visit the Acupuncture Practice Council website, www.apcouncil.org.uk</p>

  <div class="offer">Contact Mira for a free, 15-minute,<br>no-obligation consultation and find out how<br>acupuncture can help you.</div>

  <div class="contact-row">
    <span><svg class="icon" width="17" height="17" viewBox="0 0 16 16"><circle cx="8" cy="8" r="8" fill="var(--orange)"/><path d="M5.2 4.2c.4-.3.8-.2 1 .2l.6 1.2c.2.3.1.6-.2.9l-.4.3c.4.9 1.1 1.6 2 2l.3-.4c.3-.3.6-.4.9-.2l1.2.6c.4.2.5.6.2 1l-.5.6c-.4.4-1 .5-1.6.3C6.8 9.9 5.6 8.7 4.9 6.8c-.2-.6-.1-1.2.3-1.6z" fill="#fff"/></svg>07700 900412</span>
    <span><svg class="icon" width="18" height="13" viewBox="0 0 18 13"><rect width="18" height="13" fill="var(--orange)"/><path d="M0 0 9 7 18 0" stroke="#fff" stroke-width="1.3" fill="none"/></svg>thornburyclinic@mailbox.co.uk</span>
  </div>
  <div class="bottom-bar"></div>
</section>

<!-- Back card -->
<section class="card card--back">
  <svg class="hero" width="495" height="275" viewBox="0 0 495 275">
    <defs>
      <linearGradient id="family" x1="0" y1="0" x2="1" y2="1">
        <stop offset="0" stop-color="var(--garden)"/>
        <stop offset=".45" stop-color="var(--skin)"/>
        <stop offset="1" stop-color="#d9c6b8"/>
      </linearGradient>
    </defs>
    <rect role="img" aria-label="Photo of a smiling three-generation family sitting together on a sofa" width="495" height="275" fill="url(#family)"/>
    <path d="M0 180 C80 190 140 250 260 255 C360 258 430 240 495 250 L495 275 L0 275 Z" fill="var(--yellow)"/>
    <path d="M0 225 C90 232 160 272 270 273 C370 274 440 262 495 265 L495 275 L0 275 Z" fill="var(--paper)"/>
  </svg>
  <div class="wordmark">thornbury<br>accupuncture</div>

  <h2 class="section-title what-title">What is acupuncture</h2>
  <p class="section-body what-body">Acupuncture is a holistic therapy, practised for more than 2500 years in China and now popular around the world. Specific points on the body are stimulated to assist its own healing ability, balancing its energy and boosting the feeling of well-being.</p>

  <h2 class="section-title about-title">About Mira</h2>
  <div class="section-body about-body">
    <p>Mira has a passion for helping people to stay healthy by applying acupuncture, diet and lifestyle advice.</p>
    <p>She has a BSc (hons) in acupuncture and physiotherapy and 9 years’ experience working in the public health service.</p>
  </div>

  <div class="thumb thumb--back" role="img" aria-label="Photo of hands on a lower back with a sore spot"></div>
  <div class="thumb thumb--hand" role="img" aria-label="Photo of a practitioner pressing a point on a patient's hand"></div>
  <div class="thumb thumb--needles" role="img" aria-label="Photo of acupuncture needles placed on a shoulder"></div>

  <div class="portrait" role="img" aria-label="Portrait photo of the practitioner"></div>
  <div class="practitioner">
    <p class="practitioner-name">Mira Kostova</p>
    <p class="credentials">BSc (hons), LicAc, MAPC</p>
  </div>
  <ul class="contact-list">
    <li><svg class="icon" width="11" height="11" viewBox="0 0 16 16"><circle cx="8" cy="8" r="8" fill="var(--orange)"/><path d="M5.2 4.2c.4-.3.8-.2 1 .2l.6 1.2c.2.3.1.6-.2.9l-.4.3c.4.9 1.1 1.6 2 2l.3-.4c.3-.3.6-.4.9-.2l1.2.6c.4.2.5.6.2 1l-.5.6c-.4.4-1 .5-1.6.3C6.8 9.9 5.6 8.7 4.9 6.8c-.2-.6-.1-1.2.3-1.6z" fill="#fff"/></svg>07700 900412</li>
    <li><svg class="icon" width="11" height="11" viewBox="0 0 11 11"><circle cx="5.5" cy="5.5" r="5.5" fill="var(--orange)"/></svg>thornburyclinic</li>
    <li><svg class="icon" width="11" height="8" viewBox="0 0 18 13"><rect width="18" height="13" fill="var(--orange)"/><path d="M0 0 9 7 18 0" stroke="#fff" stroke-width="1.5" fill="none"/></svg>thornburyclinic@mailbox.co.uk</li>
  </ul>
  <div class="bottom-bar"></div>
</section>

</body>
</html>
```